FotoVELTA buisnesscard

Hey :) I need a modern buisnesscard for my company FotoVELTA
It most have:
Dagligleder og Fotograf: Henrik Torvald Bjelland

Mob: +4791642058
Epost: post@fotovelta.no
Adresse: Bakkestien22, 5412 Stordvik

Facbook and instagram logo with text FotoVELTA

FotoVELTA logo

It Company

```html
<!DOCTYPE html>
<html lang="no">
<head>
<meta charset="utf-8">
<title>FotoVELTA – visittkort</title>
<link rel="stylesheet" href="https://fonts.googleapis.com/css2?family=Open+Sans:wght@400;600;700&display=swap">
<style>
  :root {
    --card-blue: #03506f;
    --card-edge: #1a9fe0;
    --ink-light: #c8ccd0;
    --page: #ffffff;
  }
  * { margin: 0; padding: 0; box-sizing: border-box; }
  html, body {
    width: 1200px; height: 800px; overflow: hidden;
    background: var(--page);
    font-family: "Open Sans", Arial, sans-serif;
  }
  .sheet { position: relative; width: 1200px; height: 800px; }

  .card {
    position: absolute; left: 330px;
    width: 540px; height: 320px;
    background: var(--card-blue);
    border-bottom: 4px solid var(--card-edge);
    color: var(--ink-light);
  }
  .card--front { top: 50px; display: flex; align-items: center; justify-content: center; }
  .card--back { top: 420px; }

  .brand { font-weight: 700; letter-spacing: 0.5px; color: var(--ink-light); white-space: nowrap; }
  .card--front .brand { font-size: 40px; }
  .card--back .brand { position: absolute; left: 36px; top: 40px; font-size: 30px; }

  .holder { position: absolute; right: 36px; top: 40px; text-align: right; white-space: nowrap; }
  .holder-name { font-size: 17px; font-weight: 700; }
  .holder-role { font-size: 12px; font-weight: 600; margin-top: 2px; }

  .contact { position: absolute; right: 36px; top: 150px; list-style: none; }
  .contact li {
    display: flex; align-items: center; justify-content: flex-end;
    gap: 10px; font-size: 12px; font-weight: 600; height: 24px; white-space: nowrap;
  }
  .contact svg { width: 16px; height: 16px; flex: none; }

  .social {
    position: absolute; left: 36px; bottom: 30px;
    display: flex; align-items: center; gap: 10px;
    font-size: 12px; font-weight: 600;
  }
  .social-dot { width: 16px; height: 16px; border-radius: 50%; background: var(--ink-light); }
</style>
</head>
<body>
<main class="sheet">
  <section class="card card--front" aria-label="Visittkort forside">
    <div class="brand">FotoVELTA</div>
  </section>

  <section class="card card--back" aria-label="Visittkort bakside">
    <div class="brand">FotoVELTA</div>

    <div class="holder">
      <div class="holder-name">Henrik Torvald Bjelland</div>
      <div class="holder-role">Dagligleder og Fotograf</div>
    </div>

    <ul class="contact">
      <li>+4791642058
        <svg viewBox="0 0 16 16" aria-hidden="true"><circle cx="8" cy="8" r="8" fill="#c8ccd0"/><path d="M5.2 4.2l1.4-.2.8 2-1 .8a5 5 0 0 0 2.8 2.8l.8-1 2 .8-.2 1.4c-3.8.4-7-2.8-6.6-6.6z" fill="#03506f"/></svg>
      </li>
      <li>post@fotovelta.no
        <svg viewBox="0 0 16 16" aria-hidden="true"><circle cx="8" cy="8" r="8" fill="#c8ccd0"/><rect x="4" y="5.2" width="8" height="5.6" rx="0.6" fill="#03506f"/><path d="M4.3 5.6L8 8.4l3.7-2.8" stroke="#c8ccd0" stroke-width="0.8" fill="none"/></svg>
      </li>
      <li>Bakkestien22, 5412 Stordvik
        <svg viewBox="0 0 16 16" aria-hidden="true"><circle cx="8" cy="8" r="8" fill="#c8ccd0"/><path d="M8 3.5a3 3 0 0 0-3 3c0 2.2 3 5.8 3 5.8s3-3.6 3-5.8a3 3 0 0 0-3-3z" fill="#03506f"/><circle cx="8" cy="6.5" r="1.1" fill="#c8ccd0"/></svg>
      </li>
    </ul>

    <div class="social">
      <span class="social-dot" aria-hidden="true"></span>
      <span>FotoVELTA</span>
    </div>
  </section>
</main>
</body>
</html>
```